Harrow Creek Lodge - Boutique lodge in the Canadian Rockies

We need to re-do our website.
It is old and looks terrible.
www.harrowcreeklodge.example
We are in the process of upgrading the property, so the website needs to reflect a 4.5 star boutique mountain property. Rustic luxury. Attached is the new rooms decor concept.
Target Market(s)
skiing, snowboarding, hiking, Adventure, outdoors, couples.
Industry/Entity Type
Hotel
Logo Text
Harrow Creek Lodge
Coding
Coded - Design and coding required
Number of Pages Required
5+ page
Requirements
Must have
- Luxury, canadian rocky mountain theme.
Should not have
- Cowboy theme.

```html
<!DOCTYPE html>
<html lang="en">
<head>
<meta charset="utf-8">
<title>Harrow Creek Lodge &amp; Spa</title>
<link href="https://fonts.googleapis.com/css2?family=Raleway:wght@400;500;600&family=Roboto:wght@400;500;700&display=swap" rel="stylesheet">
<style>
:root{
  --red:#d50f1f;
  --red-deep:#b80b1a;
  --nav-active:#5a0a0f;
  --ink:#333;
  --muted:#555;
  --light:#f1f1f1;
  --line:#2c3e66;
  --footer:#3b3b3b;
  --footer-base:#262626;
  --white:#fff;
}
*{box-sizing:border-box;margin:0;padding:0}
html,body{width:1200px;height:3358px;overflow:hidden;background:var(--white)}
body{font-family:"Roboto",Arial,sans-serif;color:var(--ink);position:relative}
.header{position:relative;height:80px;background:var(--white)}
.header-contact{position:absolute;right:48px;top:30px;display:flex;gap:22px;font-size:15px;color:#333;align-items:center}
.header-contact span{display:flex;align-items:center;gap:7px}
.brand{position:absolute;left:50px;top:10px;width:170px;height:126px;background:var(--white);border:3px solid var(--red);z-index:3;display:flex;flex-direction:column;align-items:center;justify-content:center;text-align:center;gap:6px}
.brand-mark{width:22px;height:22px;background:var(--red)}
.brand-name{font-family:"Roboto",Arial,sans-serif;font-weight:700;font-size:22px;line-height:1.1;color:var(--red);text-transform:uppercase}
.nav{position:absolute;left:0;top:80px;width:1200px;height:50px;background:var(--red);z-index:2}
.nav ul{list-style:none;display:flex;position:absolute;left:251px;top:0;height:50px}
.nav li{height:50px;display:flex;align-items:center;padding:0 18px;color:var(--white);font-size:15px;margin-right:12px}
.nav li.active{background:var(--nav-active)}
.hero{position:absolute;top:130px;left:0;width:1200px;height:553px;background:linear-gradient(180deg,#9fc3e4 0%,#6e8f5a 35%,#8a5a34 60%,#4d5a35 100%)}
.welcome{position:absolute;top:683px;left:0;width:1200px;height:314px;text-align:center}
.welcome h1{font-family:"Raleway",sans-serif;font-weight:500;font-size:34px;color:#222;margin-top:26px}
.welcome p{font-size:14px;color:var(--muted);line-height:1.6;width:1050px;margin:0 auto}
.welcome p.first{margin-top:34px}
.welcome p+p{margin-top:24px}
.lodge{position:absolute;top:997px;left:0;width:1200px;height:515px;background:linear-gradient(180deg,var(--red) 0%,var(--red-deep) 100%);color:var(--white);text-align:center}
.lodge h2{font-family:"Raleway",sans-serif;font-weight:400;font-size:44px;position:absolute;top:68px;width:100%}
.feature{position:absolute;top:150px;width:250px;text-align:center}
.feature .ring{width:152px;height:152px;border:2px solid var(--white);border-radius:50%;margin:0 auto;display:flex;align-items:center;justify-content:center}
.feature h3{font-weight:400;font-size:18px;margin-top:30px}
.feature p{font-size:14px;line-height:1.6;margin-top:14px;padding:0 20px}
.gallery{position:absolute;top:1512px;left:0;width:1200px;height:727px;text-align:center}
.section-title{font-family:"Raleway",sans-serif;font-weight:400;font-size:44px;color:#222}
.gallery .section-title{margin-top:50px}
.divider{display:flex;justify-content:center;align-items:center;gap:8px;margin-top:16px}
.divider i{display:block;width:70px;height:2px;background:var(--line)}
.divider b{display:block;width:10px;height:10px;border:2px solid var(--line)}
.tile{position:absolute;width:332px;height:220px}
.tile-overlay{position:absolute;inset:14px;border:1px solid rgba(255,255,255,.6);text-align:left;color:var(--white)}
.tile-overlay h4{font-size:14px;font-weight:700;text-transform:uppercase;line-height:1.5;margin:22px 0 0 16px}
.tile-overlay .heart{position:absolute;right:18px;top:20px}
.tile-overlay .more{position:absolute;left:97px;top:138px;width:135px;height:38px;border:2px solid var(--white);display:flex;align-items:center;justify-content:center;font-size:14px;letter-spacing:.5px}
.contact{position:absolute;top:2239px;left:0;width:1200px;height:627px;background:var(--light);text-align:center}
.contact .section-title{margin-top:40px}
.contact .help{font-size:17px;font-weight:700;color:#222;margin-top:42px}
.contact .hotline{font-size:44px;font-weight:700;color:var(--red);margin-top:4px}
.field{position:absolute;height:47px;border:1px solid #ccc;background:var(--light);font-size:12px;color:#999;display:flex;align-items:center;justify-content:center}
.field.message{align-items:flex-start;justify-content:flex-start;padding:10px 14px;height:148px}
.submit{position:absolute;left:434px;top:528px;width:343px;height:50px;background:var(--red);color:var(--white);font-size:15px;font-weight:500;letter-spacing:1px;display:flex;align-items:center;justify-content:center}
.map{position:absolute;top:2866px;left:0;width:1200px;height:280px;background:linear-gradient(135deg,#e9eadf 0%,#dfe6d2 55%,#b9d3e8 100%)}
.map-pin{position:absolute;left:528px;top:88px}
.footer{position:absolute;top:3146px;left:0;width:1200px;height:130px;background:var(--footer)}
.social{position:absolute;top:40px;left:262px;display:flex;gap:22px}
.social span{width:54px;height:54px;border-radius:50%;background:#555;display:block}
.footer-base{position:absolute;top:3276px;left:0;width:1200px;height:82px;background:var(--footer-base);color:#ccc;font-size:14px;text-align:center;line-height:1.6;padding-top:18px}
</style>
</head>
<body>
<header class="header">
  <div class="brand"><span class="brand-mark"></span><span class="brand-name">Harrow Creek<br>Lodge &amp; Spa</span></div>
  <div class="header-contact">
    <span><svg width="16" height="16" viewBox="0 0 24 24"><path d="M6.6 10.8a15 15 0 006.6 6.6l2.2-2.2c.3-.3.7-.4 1-.2 1.1.4 2.3.6 3.6.6.6 0 1 .4 1 1V20c0 .6-.4 1-1 1A17 17 0 013 4c0-.6.4-1 1-1h3.5c.6 0 1 .4 1 1 0 1.3.2 2.5.6 3.6.1.3 0 .7-.2 1z" fill="#222"/></svg>(250) 555-0184</span>
    <span><svg width="18" height="14" viewBox="0 0 18 14"><rect x="0" y="0" width="18" height="14" fill="#222"/><path d="M0 0l9 7 9-7" stroke="#fff" stroke-width="1.5" fill="none"/></svg>info@harrowcreeklodge.example</span>
  </div>
</header>
<nav class="nav">
  <ul>
    <li class="active">The Lodge</li>
    <li>The Spa</li>
    <li>The Ridgeline Saloon</li>
    <li>Photo Gallery</li>
    <li>Local Activities</li>
    <li>Directions &amp; Maps</li>
  </ul>
</nav>
<div class="hero" role="img" aria-label="Timber and stone mountain lodge among tall evergreen trees"></div>

<section class="welcome">
  <h1>Welcome to Harrow Creek Lodge</h1>
  <p class="first">A traditionally built, rustic, wood and stone Boutique Mountain Lodge &amp; Spa with 11 luxurious ski-in suites within Ridgeline Peak Mountain Resort in British Columbia, Canada.</p>
  <p>All suites are lavishly appointed with traditional, hand-crafted solid wood furniture, sumptuous feather down beds, relaxing jetted baths (in some rooms) or walk-in showers, private balconies with stunning mountain views.</p>
  <p>The lodge has a huge common area, sauna, games room, library and is surrounded by endless hiking and biking trails.</p>
</section>

<section class="lodge">
  <h2>The Lodge</h2>
  <div class="feature" style="left:65px">
    <div class="ring"><svg width="64" height="64" viewBox="0 0 64 64" fill="#fff"><rect x="6" y="20" width="20" height="40"/><rect x="30" y="6" width="28" height="54"/><g fill="#d50f1f"><rect x="11" y="26" width="4" height="5"/><rect x="17" y="26" width="4" height="5"/><rect x="11" y="36" width="4" height="5"/><rect x="17" y="36" width="4" height="5"/><rect x="35" y="12" width="5" height="6"/><rect x="47" y="12" width="5" height="6"/><rect x="35" y="24" width="5" height="6"/><rect x="47" y="24" width="5" height="6"/><rect x="35" y="36" width="5" height="6"/><rect x="47" y="36" width="5" height="6"/><rect x="40" y="48" width="8" height="12"/></g></svg></div>
    <h3>Our Guest Rooms</h3>
    <p>A traditionally built, rustic, wood and stone Boutique Mountain Lodge &amp; Spa with 11 luxurious ski-in suites within</p>
  </div>
  <div class="feature" style="left:332px">
    <div class="ring"><svg width="70" height="70" viewBox="0 0 70 70" fill="none" stroke="#fff" stroke-width="4"><path d="M12 30a24 24 0 0142-12"/><path d="M58 40a24 24 0 01-42 12"/><path d="M54 8v12H42M16 62V50h12"/><text x="35" y="45" text-anchor="middle" font-family="Roboto,sans-serif" font-size="28" font-weight="700" fill="#fff" stroke="none">$</text></svg></div>
    <h3>Room Descriptions &amp; Rates</h3>
    <p>A traditionally built, rustic, wood and stone Boutique Mountain Lodge &amp; Spa with 11 luxurious ski-in suites within</p>
  </div>
  <div class="feature" style="left:607px">
    <div class="ring"><svg width="66" height="60" viewBox="0 0 66 60" fill="#fff"><path d="M6 4l2 4 4 .5-3 3 1 4-4-2-4 2 1-4-3-3 4-.5z"/><path d="M6 22l2 4 4 .5-3 3 1 4-4-2-4 2 1-4-3-3 4-.5z"/><path d="M6 40l2 4 4 .5-3 3 1 4-4-2-4 2 1-4-3-3 4-.5z"/><rect x="20" y="8" width="44" height="4"/><rect x="20" y="26" width="44" height="4"/><rect x="20" y="44" width="44" height="4"/></svg></div>
    <h3>Lodge Features</h3>
    <p>A traditionally built, rustic, wood and stone Boutique Mountain Lodge &amp; Spa with 11 luxurious ski-in suites within</p>
  </div>
  <div class="feature" style="left:867px">
    <div class="ring"><svg width="64" height="64" viewBox="0 0 64 64"><circle cx="24" cy="24" r="18" fill="none" stroke="#fff" stroke-width="4"/><circle cx="24" cy="24" r="8" fill="#fff"/><path d="M26 26l30 12-12 4 10 12-5 4-10-12-6 10z" fill="#fff" stroke="#d50f1f" stroke-width="2"/></svg></div>
    <h3>Booking Policies</h3>
    <p>A traditionally built, rustic, wood and stone Boutique Mountain Lodge &amp; Spa with 11 luxurious ski-in suites within</p>
  </div>
</section>

<section class="gallery">
  <h2 class="section-title">Our Photo Gallery</h2>
  <div class="divider"><i></i><b></b><i></i></div>
  <div class="tile" style="left:76px;top:181px;background:linear-gradient(180deg,#55585e,#3a3b3f)" role="img" aria-label="Dark timber house exterior">
    <div class="tile-overlay">
      <h4>Subway Elevation<br>California</h4>
      <svg class="heart" width="30" height="28" viewBox="0 0 30 28"><path d="M15 26S2 17 2 9a6.5 6.5 0 0113-1 6.5 6.5 0 0113 1c0 8-13 17-13 17z" fill="none" stroke="#fff" stroke-width="2"/></svg>
      <div class="more">VIEW MORE</div>
    </div>
  </div>
  <div class="tile" style="left:434px;top:181px;background:linear-gradient(135deg,#e6e4e0,#b9b2a8)" role="img" aria-label="Bright bathroom with vanity and glass shower"></div>
  <div class="tile" style="left:795px;top:181px;background:linear-gradient(135deg,#d7e3e8,#eadcd8)" role="img" aria-label="Pastel bedroom with a colourful bedspread"></div>
  <div class="tile" style="left:76px;top:431px;background:linear-gradient(180deg,#8fb6da 0%,#3c3c40 45%,#5d8a3a 100%)" role="img" aria-label="Dark house with a green front lawn"></div>
  <div class="tile" style="left:434px;top:431px;background:linear-gradient(135deg,#d9d6d0,#6e6559)" role="img" aria-label="Living room with stone fireplace and armchair"></div>
  <div class="tile" style="left:795px;top:431px;background:linear-gradient(180deg,#c9dcea 0%,#8a7a66 50%,#7a9a5a 100%)" role="img" aria-label="Stone and timber house with a double garage"></div>
</section>

<section class="contact">
  <h2 class="section-title">Contact Form</h2>
  <div class="divider"><i></i><b></b><i></i></div>
  <p class="help">NEED HELP? CALL US</p>
  <p class="hotline">+800 555 0199</p>
  <div class="field" style="left:65px;top:280px;width:343px">Name</div>
  <div class="field" style="left:434px;top:280px;width:341px">Email</div>
  <div class="field" style="left:804px;top:280px;width:340px">Phone</div>
  <div class="field message" style="left:65px;top:354px;width:1079px">Message</div>
  <div class="submit">SUBMIT</div>
</section>

<div class="map" role="img" aria-label="Road map of the area around the lodge">
  <svg class="map-pin" width="26" height="36" viewBox="0 0 26 36"><path d="M13 35S2 20 2 12a11 11 0 0122 0c0 8-11 23-11 23z" fill="#e2342a"/><circle cx="13" cy="12" r="4" fill="#8a1610"/></svg>
</div>

<footer class="footer">
  <div class="social"><span></span><span></span><span></span><span></span><span></span><span></span><span></span><span></span></div>
</footer>
<div class="footer-base">All Rights Reserved Design by my company<br>2013 - 2017 © The Harrow Creek Lodge</div>
</body>
</html>
```